Postcard Design

I am a practicing Obstetrician and Gynecologist. I am working at a clinic called Corvane Ridge Health System. I am looking for a design of a personal advertisement card that can be mailed, handed out, or sent an an electronic copy to the local newspaper to be placed as an ad. I previously worked for another clinic called TBW. They had an ad on my I liked very much, but I cannot use it. It is proprietary to them. I would like something like it. Copy attached. I want my foto and text. I have Printhollow Business Cards with Corvane Ridge and Stationary already. Access permitted. I would like to stay within that light blue - light green color scheme. I want the card to have me come across as competent and knowledgeable, but also as gentle, compassionate, benevolent, caring, knowledgeable, competent. Obviously, it has to appeal to women.

Target Market(s)

Public, patients, women

Industry/Entity Type

Electronic

Requirements
Nice to have
• A sophisticated, tasteful and inspiring maternity care image is very hard to find. I love the one on my business card. If it or something like it could be found and incorporated, that would be nice. I like a warm, soft, friendly font, Calibri light italic, Archer, Gotham. Describes nicely:Archer, the colorful slab serif. Sweet but not saccharine, earnest but not grave, Archer is designed to hit just the right notes of forthrightness, credibility, and charm.

```html
<!DOCTYPE html>
<html lang="en">
<head>
<meta charset="utf-8">
<title>Dr. Matthias R. Halvorsen – OB/GYN Postcard</title>
<link rel="stylesheet" href="https://fonts.googleapis.com/css2?family=Jost:ital,wght@0,400;0,500;0,600;0,700;1,400;1,700&display=swap">
<style>
  :root {
    --ink: #111111;
    --panel: rgba(255, 255, 255, 0.9);
    --band: rgba(255, 255, 255, 0.88);
    --sky-top: #c9d6de;
    --sky-glow: #f4ead0;
    --haze: #e6eee6;
    --field: #a8c860;
    --field-bright: #dfe23a;
    --coat: #f4f5f6;
    --coat-shade: #dcdfe2;
  }
  * { box-sizing: border-box; margin: 0; padding: 0; }
  html, body { width: 1200px; height: 926px; overflow: hidden; background: #ffffff; }
  body { font-family: "Jost", "Futura", sans-serif; color: var(--ink); }

  .postcard { position: relative; width: 1200px; height: 926px; overflow: hidden; }

  .backdrop {
    position: absolute; inset: 0;
    background: linear-gradient(180deg, var(--sky-top) 0%, var(--sky-glow) 30%, var(--haze) 52%, var(--field) 78%, var(--field-bright) 100%);
  }

  .portrait {
    position: absolute; top: 0; right: 0; width: 560px; height: 926px;
    background:
      radial-gradient(ellipse 150px 190px at 340px 250px, #e7c9b6 0%, #d9b39d 60%, rgba(217,179,157,0) 100%),
      radial-gradient(ellipse 330px 420px at 330px 760px, var(--coat) 0%, var(--coat) 70%, rgba(244,245,246,0) 100%),
      linear-gradient(90deg, rgba(255,255,255,0) 0%, rgba(230,234,236,0.7) 30%, var(--coat-shade) 100%);
  }

  .info-panel {
    position: absolute; left: 34px; top: 50px; width: 662px; height: 717px;
    background: var(--panel);
    padding: 36px 26px 0 28px;
  }

  .doctor-name {
    text-align: center; font-weight: 700; font-size: 33px; letter-spacing: 0; line-height: 1.1;
    white-space: nowrap;
  }
  .doctor-name .nickname { font-style: italic; }
  .credentials { text-align: center; font-size: 30px; font-weight: 400; line-height: 1.25; margin-top: 4px; }
  .specialty { text-align: center; font-size: 20px; letter-spacing: 0.4px; margin-top: 0; }

  .bio, .focus, .training, .contact { font-size: 19.5px; letter-spacing: 0.7px; }
  .bio, .focus { line-height: 28.5px; text-align: justify; margin-top: 24px; }
  .bio strong { font-weight: 700; }
  .focus { text-align: left; margin-top: 29px; }

  .training { line-height: 28.5px; margin-top: 29px; }
  .training dt { font-weight: 700; }

  .contact { display: flex; margin-top: 32px; line-height: 28.5px; }
  .contact .location { width: 296px; font-style: normal; white-space: nowrap; }
  .contact .location strong, .contact .phone { font-weight: 700; }
  .contact .fax { margin-top: 28.5px; }

  .insurance-band {
    position: absolute; left: 0; top: 835px; width: 1200px; height: 80px;
    background: var(--band);
    padding: 13px 38px 0;
    font-style: italic; font-size: 18.5px; line-height: 27px; letter-spacing: 0.2px;
    white-space: nowrap;
  }
</style>
</head>
<body>
<main class="postcard">
  <div class="backdrop" role="img" aria-label="Soft sunlit sky over a bright green and yellow meadow"></div>
  <div class="portrait" role="img" aria-label="Portrait photo of the smiling doctor in a white coat"></div>

  <section class="info-panel">
    <h1 class="doctor-name">MATTHIAS R. <span class="nickname">(“ MATT ”)</span> HALVORSEN</h1>
    <p class="credentials">MD, FACOG</p>
    <p class="specialty">BOARD CERTIFIED OBSTETRICIAN &amp; GYNECOLOGIST</p>

    <p class="bio"><strong>Dr. Halvorsen</strong> is a Board Certified OB/GYN and was in private practice in Atlanta, Georgia for twenty-five years. He recently was the in-house hospitalist Obstetrics and Gynecology at the Harbor Bay Memorial Hospital.</p>

    <dl class="training">
      <dt>Education:</dt>
      <dd>Nordhafen University School of Medicine, Germany</dd>
      <dt>Residency and Internship:</dt>
      <dd>Eastbrook University School of Medicine, New York</dd>
      <dd><strong>Residency:</strong> Riverton University School of Medicine, Kentucky</dd>
    </dl>

    <p class="focus">Dr. Halvorsen specializes in preventive medicine and women’s wellness and weight management</p>

    <div class="contact">
      <address class="location">
        <strong>Accepting New Patients at</strong><br>
        Corvane Ridge Health System<br>
        214-B Lantern Cove Road<br>
        Marisol Bay, GU 96900
      </address>
      <div class="appointments">
        Please call for an appointment at<br>
        <span class="phone">671-555-0142</span>
        <p class="fax">Fax: 671-555-0187</p>
      </div>
    </div>
  </section>

  <footer class="insurance-band">
    CREDENTIALED PROVIDER WITH MERIDIAN GLOBAL, BLUECREST / SHIELDWELL, MARLOWE’S CHOICECARE, CIVICARE, AGEWELL,<br>
    OIP, LINKCARE, KEEPWELL, FIRSTCARE, TRIGUARD.&nbsp; REFERRAL REQUIRED WITH SOME PLANS.
  </footer>
</main>
</body>
</html>
```